Business Card Design Project

I am community manager and social media strategist. I need a double sided business card with company logo and name. Looking for something professional, elegant but also a little bit original.

• - The logo and the colours are the company colours and a required to stay.
- The size should be: 84 x 55 mm (or 3.30 x 2.16)
- The file size should be: 1039 x 697 pixels (300 dpi)
- I'd like rounded corners. :)

Use the following contact information for the card:

Léonie Vardin
Stratégie médias sociaux / community management / édition de sites sociaux
mob. : 0687529103
leonie.vardin@postelune.fr
Twitter. : @lvardin
Skype : vardin.leonie

```html
<!DOCTYPE html>
<html lang="en">
<head>
<meta charset="utf-8">
<title>Postelune business card</title>
<link rel="stylesheet" href="https://fonts.googleapis.com/css2?family=Arimo:wght@400;700&display=swap">
<style>
  :root {
    --backdrop: #2b3438;
    --card-white: #ffffff;
    --brand-blue: #1a6aa8;
    --brand-deep: #0e4f86;
    --brand-light: #2f86c6;
    --ink: #3a3a3a;
    --ink-soft: #4a4a4a;
  }
  * { margin: 0; padding: 0; box-sizing: border-box; }
  html, body {
    width: 1200px;
    height: 846px;
    overflow: hidden;
    background: var(--backdrop);
    font-family: "Arimo", Arial, sans-serif;
  }
  .stage {
    position: relative;
    width: 1200px;
    height: 846px;
  }
  .card {
    position: absolute;
    top: 246px;
    width: 540px;
    height: 354px;
    border-radius: 16px;
    background: var(--card-white);
    overflow: hidden;
    box-shadow: 0 6px 18px rgba(0,0,0,0.35);
  }
  .card--front { left: 40px; }
  .card--back  { left: 620px; }

  /* Front side */
  .front-mark {
    position: absolute;
    left: 40px;
    top: 0;
    height: 100%;
    display: flex;
    align-items: center;
    gap: 26px;
  }
  .front-mark__dot {
    width: 150px;
    height: 150px;
    border-radius: 50%;
    background: var(--brand-blue);
  }
  .front-mark__name {
    font-weight: 700;
    font-size: 44px;
    letter-spacing: 2px;
    color: var(--brand-blue);
  }

  /* Back side */
  .back-info {
    position: absolute;
    left: 0;
    top: 0;
    width: 270px;
    height: 100%;
  }
  .back-info__name {
    position: absolute;
    left: 40px;
    top: 50px;
    font-weight: 700;
    font-size: 20px;
    color: var(--ink);
  }
  .back-info__role {
    position: absolute;
    left: 40px;
    top: 76px;
    font-size: 16px;
    color: var(--brand-light);
  }
  .back-info__address {
    position: absolute;
    left: 36px;
    top: 136px;
    font-size: 16px;
    line-height: 22px;
    color: var(--ink-soft);
  }
  .back-info__accent {
    position: absolute;
    left: 0;
    top: 216px;
    width: 10px;
    height: 106px;
    background: linear-gradient(to bottom, var(--brand-light), var(--brand-deep));
  }
  .contact-list {
    position: absolute;
    left: 40px;
    top: 218px;
    list-style: none;
  }
  .contact-list__item {
    display: flex;
    align-items: center;
    gap: 8px;
    height: 25px;
    font-size: 15px;
    color: var(--ink);
    white-space: nowrap;
  }
  .contact-list__icon {
    width: 14px;
    height: 14px;
    flex: none;
  }
  .contact-list__badge {
    width: 12px;
    height: 12px;
    margin: 0 1px;
    border-radius: 50%;
    background: var(--brand-blue);
    flex: none;
  }
  .back-panel {
    position: absolute;
    left: 270px;
    top: 0;
    width: 270px;
    height: 100%;
    background: linear-gradient(to right, var(--brand-blue), var(--brand-deep));
    display: flex;
    flex-direction: column;
    align-items: center;
    justify-content: center;
    gap: 18px;
  }
  .back-panel__dot {
    width: 80px;
    height: 80px;
    border-radius: 50%;
    background: var(--card-white);
  }
  .back-panel__name {
    font-weight: 700;
    font-size: 32px;
    letter-spacing: 1.5px;
    color: var(--card-white);
  }
</style>
</head>
<body>
<main class="stage">
  <section class="card card--front" aria-label="Card front">
    <div class="front-mark">
      <span class="front-mark__dot"></span>
      <span class="front-mark__name">POSTELUNE</span>
    </div>
  </section>

  <section class="card card--back" aria-label="Card back">
    <div class="back-info">
      <p class="back-info__name">Léonie Vardin</p>
      <p class="back-info__role">Director</p>
      <p class="back-info__address">18 Harbour Lane,<br>Victoria 3008<br>Melbourne, Australia</p>
      <span class="back-info__accent"></span>
      <ul class="contact-list">
        <li class="contact-list__item">
          <svg class="contact-list__icon" viewBox="0 0 14 14" aria-hidden="true">
            <rect x="3.5" y="0.5" width="7" height="13" rx="1.6" fill="none" stroke="#1a6aa8" stroke-width="1.4"/>
            <rect x="5" y="2.5" width="4" height="6" fill="#1a6aa8"/>
          </svg>
          0687529103
        </li>
        <li class="contact-list__item">
          <svg class="contact-list__icon" viewBox="0 0 14 14" aria-hidden="true">
            <rect x="0.5" y="3" width="13" height="8.5" fill="#1a6aa8"/>
            <path d="M0.5 3 L7 8 L13.5 3" fill="none" stroke="#ffffff" stroke-width="1.2"/>
          </svg>
          leonie.vardin@postelune.fr
        </li>
        <li class="contact-list__item">
          <span class="contact-list__badge"></span>
          @lvardin
        </li>
        <li class="contact-list__item">
          <span class="contact-list__badge"></span>
          vardin.leonie
        </li>
      </ul>
    </div>
    <div class="back-panel">
      <span class="back-panel__dot"></span>
      <span class="back-panel__name">POSTELUNE</span>
    </div>
  </section>
</main>
</body>
</html>
```